Calloway Pipeworks Summary ESG brochure report

We are looking to create a summary ESG report for and Oil and Gas Midstream producer - Calloway Pipeworks. This is a report on their environmental, social and governance (ESG) aspects as well as a summary of who they are. It's focused on Wyoming oil and gas midstream for pipeline transport of oil and gas. We are to emphasize their environmental aspects, social aspects with visuals, graphics, etc. Attached is a example ESG report that is larger than what we want, but gives the designer of what an ESG report is.
The attached Harrowgate 2019 report is an "IDEA of what we are looking for - but on a smaller scale. This is a much larger report, but expands on the idea of what we are trying to do.
Client is:
https://www.callowaypipeworks.example/
The outline brochure documens is what we have written and given examples of graphics with our writing / bullets of what we have visioned through the brochure. We are looking for a document with these items and graphs in it.
We have attached a few excel sheets and creations to hopefully better visualize our ideas and timelines to assist the graphic designers.
Look and feel
Each slider illustrates characteristics of the customer's brand and the style your logo design should communicate.

```html
<!DOCTYPE html>
<html lang="en">
<head>
<meta charset="utf-8">
<title>Calloway Pipeworks — Environment</title>
<link href="https://fonts.googleapis.com/css2?family=Poppins:wght@400;500&family=Lato:wght@400;700&family=Montserrat:wght@600;700&display=swap" rel="stylesheet">
<style>
  :root {
    --navy: #0c1d4a;
    --steel: #5a7f98;
    --band: #5b8199;
    --ink: #1a1a1a;
    --white: #ffffff;
    --rule: #1a1a1a;
  }
  * { margin: 0; padding: 0; box-sizing: border-box; }
  html, body { width: 848px; height: 1200px; overflow: hidden; background: var(--white); }
  .page { position: relative; width: 848px; height: 1200px; overflow: hidden; background: var(--white); }

  .section-title {
    position: absolute;
    font-family: "Poppins", sans-serif;
    font-weight: 400;
    font-size: 22px;
    line-height: 1;
  }
  .section-rule { position: absolute; height: 2px; width: 120px; }

  .env-title { left: 48px; top: 52px; color: var(--ink); }
  .env-rule { left: 48px; top: 93px; background: var(--rule); }
  .env-copy {
    position: absolute; left: 48px; top: 124px; width: 745px;
    font-family: "Lato", sans-serif; font-size: 13px; line-height: 23.3px;
    color: var(--ink); text-align: justify;
  }

  .landscape-photo {
    position: absolute; left: 0; top: 323px; width: 848px; height: 354px;
    background: linear-gradient(180deg, #b9a9a6 0%, #9aa7ad 14%, #6f8f96 24%, #3f7a6b 36%, #2f7e4c 55%, #2f8a33 78%, #3b8f2a 100%);
  }

  .emissions-panel {
    position: absolute; left: 0; top: 677px; width: 324px; height: 499px;
    background: var(--navy);
  }
  .emi-title { left: 48px; top: 740px; color: var(--white); }
  .emi-rule { left: 48px; top: 781px; background: var(--white); }
  .emi-copy {
    position: absolute; left: 48px; top: 807px; width: 237px;
    font-family: "Lato", sans-serif; font-size: 13.5px; line-height: 23.4px;
    color: var(--white); text-align: justify;
  }

  .emissions-diagram { position: absolute; left: 324px; top: 677px; width: 524px; height: 499px; }
  .node-label {
    font-family: "Montserrat", sans-serif; font-weight: 700; font-size: 8.5px;
    letter-spacing: 1px; fill: var(--navy);
  }
  .hub-label { font-family: "Montserrat", sans-serif; font-weight: 600; font-size: 15px; letter-spacing: 1px; fill: var(--white); }

  .footer-band { position: absolute; left: 0; top: 1176px; width: 848px; height: 24px; background: var(--band); }
</style>
</head>
<body>
<main class="page">
  <h1 class="section-title env-title">Environment</h1>
  <div class="section-rule env-rule"></div>
  <p class="env-copy">We recognize that climate change is a prevalent global issue and that the world is transitioning to a lower-carbon future. We believe environmental stewardship is needed understand potential climate change risks to our business, so we can reduce our negative impacts, increase our positive impacts, and maintain our focus on our economic viability. We are committed to being proactive in our environmental work, utilizing Industry Best Practices, operating equipment efficiently, minimizing our emissions, and purchasing new low-carbon equipment, so we can avoid resources issues and mitigate negative issues resulting from our projects.</p>

  <div class="landscape-photo" role="img" aria-label="Forested green mountain ridges under a soft dusk sky"></div>

  <section class="emissions-panel"></section>
  <h2 class="section-title emi-title">Emissions</h2>
  <div class="section-rule emi-rule"></div>
  <p class="emi-copy">As environmental stewards, we are committed to reducing our greenhouse gas (GHG) and non-GHG emissions to protect the environment and safeguard our stakeholders while we continue to operate safely and efficiently and transport our customers’ products to market. To track our emissions and measure our performance, we developed a reporting approach that includes mandatory and voluntary reporting requirements.</p>

  <svg class="emissions-diagram" width="524" height="499" viewBox="0 0 524 499" aria-label="Emissions reduction levers">
    <g stroke="var(--steel)" stroke-width="1" stroke-dasharray="2 3" fill="var(--steel)">
      <line x1="174" y1="183" x2="226" y2="207"/>
      <line x1="338" y1="183" x2="288" y2="207"/>
      <line x1="182" y1="287" x2="228" y2="255"/>
      <line x1="336" y1="270" x2="290" y2="243"/>
    </g>
    <g fill="var(--steel)">
      <circle cx="174" cy="183" r="2"/><circle cx="226" cy="207" r="2"/>
      <circle cx="338" cy="183" r="2"/><circle cx="288" cy="207" r="2"/>
      <circle cx="182" cy="287" r="2"/><circle cx="228" cy="255" r="2"/>
      <circle cx="336" cy="270" r="2"/><circle cx="290" cy="243" r="2"/>
      <circle cx="143" cy="145" r="40"/>
      <circle cx="373" cy="145" r="40"/>
      <circle cx="262" cy="217" r="42"/>
      <circle cx="150" cy="305" r="40"/>
      <circle cx="373" cy="291" r="40"/>
    </g>
    <text class="hub-label" x="262" y="223" text-anchor="middle">C02</text>

    <!-- vehicle icon -->
    <g fill="var(--white)">
      <rect x="121" y="129" width="28" height="22" rx="1"/>
      <path d="M151 136h10l6 8v7h-16z"/>
      <circle cx="129" cy="155" r="4"/><circle cx="159" cy="155" r="4"/>
    </g>
    <!-- fleet renewal icon -->
    <g fill="var(--white)">
      <rect x="351" y="129" width="28" height="22" rx="1"/>
      <path d="M381 136h10l6 8v7h-16z"/>
      <circle cx="359" cy="155" r="4"/><circle cx="389" cy="155" r="4"/>
      <circle cx="365" cy="140" r="6" fill="none" stroke="var(--steel)" stroke-width="1.8" stroke-dasharray="14 4"/>
    </g>
    <!-- droplet icon -->
    <path d="M150 282c-9 13-15 21-15 28a15 15 0 0 0 30 0c0-7-6-15-15-28z" fill="var(--white)"/>
    <path d="M143 310a7 7 0 0 0 6 8" fill="none" stroke="var(--steel)" stroke-width="2" stroke-linecap="round"/>
    <!-- gear icon -->
    <g transform="translate(373 291)" fill="var(--white)">
      <circle r="13"/>
      <g>
        <rect x="-3.5" y="-18" width="7" height="8" rx="1"/>
        <rect x="-3.5" y="-18" width="7" height="8" rx="1" transform="rotate(45)"/>
        <rect x="-3.5" y="-18" width="7" height="8" rx="1" transform="rotate(90)"/>
        <rect x="-3.5" y="-18" width="7" height="8" rx="1" transform="rotate(135)"/>
        <rect x="-3.5" y="-18" width="7" height="8" rx="1" transform="rotate(180)"/>
        <rect x="-3.5" y="-18" width="7" height="8" rx="1" transform="rotate(225)"/>
        <rect x="-3.5" y="-18" width="7" height="8" rx="1" transform="rotate(270)"/>
        <rect x="-3.5" y="-18" width="7" height="8" rx="1" transform="rotate(315)"/>
      </g>
      <circle r="5.5" fill="var(--steel)"/>
    </g>

    <text class="node-label" text-anchor="middle"><tspan x="132" y="204">VEHICLE-RELATED</tspan><tspan x="132" y="214">MEASURES</tspan></text>
    <text class="node-label" text-anchor="middle" x="377" y="204">FLEET RENEWAL</text>
    <text class="node-label" text-anchor="middle"><tspan x="152" y="355">ALTERNATIVE</tspan><tspan x="152" y="365">FUELS</tspan></text>
    <text class="node-label" text-anchor="middle" x="373" y="355">OPERATIONS</text>
  </svg>

  <div class="footer-band"></div>
</main>
</body>
</html>
```